Yacht, Boats, Watersports company needs a redesign of business card

Hello Designers!
We are a Boat dealership company that sells fun in the water, we sell boats, Yachts, Kayaks and also yacht WaterSport toys. We are looking to redesign our business cards in to something a little bit more sophisticated. in a way that we can make better use of our company colors. I'm attaching a zipped file containing the company 3 sets of company logo which one is an horizontal another one is a vertical and also a chromed 3d logo. Also is included two set of business cards that we use and also some designs that i think it's interesting. We use PMS 2026c Orange and PMS 7687C Blue. I would like to see at least two different options with the orange as accent and also using blue as an accent color. It's really important for the business cards to have a font option and size that is legible to most people. Our current website is wwww.corvellamarine.com. Please visit if you want to have a better feeling of the Boat dealership
You can send Single sided or double side options. We are now using single sided but we may be open for a double side option if we really like the design.
Target Market(s)
Marine, boat sales, yacht sales, water toys sales/
Contact Information for Business Card
Name: Dale Pritchett
Address: 718 West Halden Lane,
Dania Beach, FL 33019
Phone: 954-382-7146
Fax: 954:382-7139
Cell: 954-451-8320
Email: 212@corvellamarine.com
Website: corvellamarine.com
Requirements
Must have
- the current information of the business card provided.
logo
use the PMS Colors
Nice to have
- a touch of elegance and sophistication but simple
Should not have
- should not have any typography that is hard to read, the card should be simple but yet sophisticated.

```html
<!DOCTYPE html>
<html lang="en">
<head>
<meta charset="utf-8">
<title>Corvella Marine business card</title>
<link rel="stylesheet" href="https://fonts.googleapis.com/css2?family=Arimo:wght@400;700&display=swap">
<style>
  :root {
    --backdrop: #1b1b1b;
    --card-blue: #1f4580;
    --accent-orange: #f04e23;
    --ink-white: #ffffff;
  }
  * { margin: 0; padding: 0; box-sizing: border-box; }
  html, body {
    width: 1200px; height: 988px; overflow: hidden;
    background: var(--backdrop);
    font-family: "Arimo", Arial, sans-serif;
  }
  .canvas { position: relative; width: 1200px; height: 988px; }
  .card {
    position: absolute;
    width: 620px; height: 354px;
    background: var(--card-blue);
    border-radius: 22px;
    box-shadow: 0 14px 30px rgba(0,0,0,.55);
    color: var(--ink-white);
  }
  .card--front { left: 60px; top: 80px; }
  .card--back  { left: 520px; top: 554px; }

  .brand {
    position: absolute;
    display: flex; align-items: center; gap: 14px;
  }
  .brand__dot {
    width: 40px; height: 40px; border-radius: 50%;
    background: var(--accent-orange); flex: none;
  }
  .brand__name {
    font-weight: 700; color: var(--ink-white);
    letter-spacing: .12em; text-transform: uppercase;
    white-space: nowrap;
  }
  .card--front .brand { left: 50%; top: 50%; transform: translate(-50%, -50%); }
  .card--front .brand__name { font-size: 36px; }

  .card--back .brand { left: 40px; top: 50%; transform: translateY(-50%); gap: 10px; }
  .card--back .brand__dot { width: 28px; height: 28px; }
  .card--back .brand__name { font-size: 21px; }

  .divider {
    position: absolute; left: 338px; top: 70px;
    width: 1.5px; height: 214px; background: var(--accent-orange);
  }
  .contact { position: absolute; left: 362px; top: 70px; }
  .contact__name {
    font-size: 23px; font-weight: 700; color: var(--accent-orange);
    text-transform: uppercase; letter-spacing: .01em; margin-bottom: 10px;
  }
  .contact__address { font-size: 13.5px; line-height: 1.3; margin-bottom: 8px; }
  .contact__list { list-style: none; font-size: 13.5px; line-height: 1.45; }
  .contact__list li { display: flex; align-items: center; gap: 8px; }
  .contact__icon { width: 11px; height: 11px; flex: none; }
</style>
</head>
<body>
<main class="canvas">
  <section class="card card--front" aria-label="Card front">
    <div class="brand">
      <span class="brand__dot"></span>
      <span class="brand__name">Corvella Marine</span>
    </div>
  </section>

  <section class="card card--back" aria-label="Card back">
    <div class="brand">
      <span class="brand__dot"></span>
      <span class="brand__name">Corvella Marine</span>
    </div>
    <span class="divider"></span>
    <div class="contact">
      <h1 class="contact__name">Dale Pritchett</h1>
      <p class="contact__address">718 West Halden Lane,<br>Dania Beach, FL 33019</p>
      <ul class="contact__list">
        <li>
          <svg class="contact__icon" viewBox="0 0 12 12"><rect x="3" y="0.5" width="6" height="11" rx="1" fill="none" stroke="#f04e23" stroke-width="1.3"/></svg>
          954-382-7146
        </li>
        <li>
          <svg class="contact__icon" viewBox="0 0 12 12"><path d="M2 1l2.5 0 1 3-1.5 1a7 7 0 0 0 3 3l1-1.5 3 1V11C6 11 1 6 1 2z" fill="#f04e23"/></svg>
          954-451-8320
        </li>
        <li>
          <svg class="contact__icon" viewBox="0 0 12 12"><rect x="3" y="1" width="6" height="3" fill="#f04e23"/><rect x="1" y="4.5" width="10" height="4.5" rx="1" fill="#f04e23"/><rect x="3" y="8" width="6" height="3" fill="#f04e23"/></svg>
          954:382-7139
        </li>
        <li>
          <svg class="contact__icon" viewBox="0 0 12 12"><rect x="0.5" y="2" width="11" height="8" fill="#f04e23"/><path d="M0.5 2l5.5 4.5L11.5 2" fill="none" stroke="#1f4580" stroke-width="1"/></svg>
          212@corvellamarine.com
        </li>
        <li>
          <svg class="contact__icon" viewBox="0 0 12 12"><circle cx="6" cy="6" r="5.3" fill="#f04e23"/><path d="M0.7 6h10.6M6 0.7c-3 3-3 7.6 0 10.6M6 0.7c3 3 3 7.6 0 10.6" fill="none" stroke="#1f4580" stroke-width=".8"/></svg>
          wwww.corvellamarine.com
        </li>
      </ul>
    </div>
  </section>
</main>
</body>
</html>
```